Holiday/6-Mo. Firm Anniversary Graphic for E-mail to Clients

Here is the proposed text:
2 Reasons to Celebrate:
Happy New Year 2024
&
The 6-Month Anniversary
Of
Thornbury Law Offices
Focusing on Commercial Litigation,
Real Estate,Telecom and Healthcare
Disputes
I think what I would like is a static graphic that would be something that I send to
clients celebrating my law firm’s 6-month anniversary (around the first of the year so a New Year theme could be incorporated maybe). Maybe something with a picture of my face along with a cartoon/graphic body of me doing something lawyerly. Something simple but unique and maybe humorous. Then something referencing the 6-month anniversary. I don’t anything like sound or sound effect. I am not very creative, sorry. Attached are a few headshots we might use.
Target Market(s)
Current clients and future clients with prior relationships
Look and feel

```html
<!DOCTYPE html>
<html lang="en">
<head>
<meta charset="utf-8">
<title>Thornbury Law – 6-Month Anniversary</title>
<link rel="stylesheet" href="https://fonts.googleapis.com/css2?family=Cinzel:wght@400;700&family=Monsieur+La+Doulaise&display=swap">
<style>
  :root {
    --night-deep: #02060f;
    --night-mid: #08183a;
    --night-glow: #15356d;
    --gold: #d8bf8a;
    --gold-soft: rgba(232, 205, 150, 0.55);
    --white: #ffffff;
    --portrait-ring: #c9ccd2;
    --portrait-bg: #4b5f7c;
  }
  html, body {
    margin: 0;
    padding: 0;
    overflow: hidden;
    background: var(--night-deep);
  }
  .card {
    position: relative;
    width: 1200px;
    height: 1059px;
    overflow: hidden;
    background:
      radial-gradient(ellipse 70% 55% at 55% 15%, var(--night-glow) 0%, var(--night-mid) 45%, var(--night-deep) 100%);
    font-family: "Cinzel", serif;
    color: var(--white);
  }
  .fireworks {
    position: absolute;
    inset: 0 0 300px 0;
    background:
      radial-gradient(circle at 195px 300px, rgba(232,200,140,0.32) 0, rgba(232,200,140,0.12) 120px, transparent 200px),
      radial-gradient(circle at 458px 98px, rgba(245,225,185,0.38) 0, rgba(245,225,185,0.1) 50px, transparent 80px),
      radial-gradient(circle at 690px 143px, rgba(235,215,175,0.35) 0, rgba(235,215,175,0.1) 90px, transparent 135px),
      radial-gradient(circle at 950px 165px, rgba(220,200,165,0.28) 0, rgba(220,200,165,0.08) 110px, transparent 165px),
      radial-gradient(circle at 840px 440px, rgba(240,215,170,0.35) 0, rgba(240,215,170,0.1) 120px, transparent 175px),
      radial-gradient(circle at 405px 510px, rgba(235,200,140,0.3) 0, rgba(235,200,140,0.08) 60px, transparent 95px);
  }
  .portrait {
    position: absolute;
    left: 438px;
    top: 225px;
    width: 318px;
    height: 318px;
    border-radius: 50%;
    border: 4px solid var(--portrait-ring);
    background: radial-gradient(circle at 50% 40%, #8c7f7a 0%, #5d6a80 45%, var(--portrait-bg) 100%);
  }
  .firm-name {
    position: absolute;
    top: 604px;
    left: 0;
    width: 100%;
    margin: 0;
    text-align: center;
    font-weight: 700;
    font-size: 64px;
    line-height: 1;
    letter-spacing: 1px;
  }
  .tagline {
    position: absolute;
    left: 0;
    width: 100%;
    margin: 0;
    text-align: center;
    font-weight: 400;
    line-height: 1;
  }
  .tagline--first { top: 722px; font-size: 46px; }
  .tagline--second { top: 808px; font-size: 50px; padding-right: 0; }
  .mascot {
    position: absolute;
    left: 22px;
    top: 722px;
    width: 218px;
    height: 322px;
    border-radius: 40% 40% 12% 12%;
    background: linear-gradient(180deg, #d9a58a 0%, #2c3e6a 35%, #23345a 70%, #b8914a 100%);
  }
  .greeting-rule {
    position: absolute;
    left: 157px;
    top: 957px;
    width: 1015px;
    height: 4px;
    background: linear-gradient(90deg, transparent 0%, var(--gold) 8%, var(--gold) 85%, transparent 100%);
  }
  .greeting {
    position: absolute;
    left: 322px;
    top: 880px;
    margin: 0;
    font-family: "Monsieur La Doulaise", cursive;
    font-weight: 400;
    font-size: 104px;
    line-height: 1.1;
    color: var(--gold);
    text-shadow: 0 0 6px var(--night-deep), 0 0 14px var(--night-deep);
    white-space: nowrap;
  }
</style>
</head>
<body>
  <main class="card">
    <div class="fireworks" role="img" aria-label="Golden fireworks bursting across the night sky"></div>
    <div class="portrait" role="img" aria-label="Round headshot of the firm's attorney in a suit and red tie"></div>
    <h1 class="firm-name">THORNBURY LAW</h1>
    <p class="tagline tagline--first">IS CELEBRATING ITS</p>
    <p class="tagline tagline--second">6-MONTH ANNIVERSARY!</p>
    <div class="greeting-rule"></div>
    <p class="greeting">Happy New Year</p>
    <div class="mascot" role="img" aria-label="Cartoon attorney in a navy suit holding a law book and the scales of justice"></div>
  </main>
</body>
</html>
```